Clothing range for the petite modern mature woman needs a card design

We need a business card design for a new Sydney based company called plum twist. We provide clothing to the modern mature woman who finds it difficult to source clothes that do not make them look frumpy or do not fit. We have an idea we would like an apple with the peel unravelling and possibly the silhouette of a woman's body coming out of the peel. The plum twist represents the womans body shape and dressing it.

Target Market(s)

modern mature aged woman

Industry/Entity Type

Clothing

Contact Information for Business Card

abn: 41027395816
will provide email at a later date
a spiel re clothes for modern woman???

Font styles to use
Serif
Sans Serif

Requirements
Must have
• will need name - ABN -will need email address but still working on that (TBA)
Nice to have
• picture of an apple with its peel coming off and possibly the silhouette of a woman coming out. the issue a lot of women in the over 50 range have is that the clothing is very dated or makes the woman frumpy. we are providing clothes for the woman who has difficulty in finding fashionable clothes in their size.
Should not have
• don't want childlike

```html
<!DOCTYPE html>
<html lang="en">
<head>
<meta charset="utf-8">
<title>Plum Twist — Business Card</title>
<link href="https://fonts.googleapis.com/css2?family=Marcellus&family=Didact+Gothic&display=swap" rel="stylesheet">
<style>
  :root {
    --canvas: #ffffff;
    --blush: #fbd3c3;
    --leaf: #5aa83a;
    --band: #72bb4c;
    --mark: #7cc35a;
    --white: #ffffff;
  }
  html, body {
    margin: 0;
    padding: 0;
    width: 1200px;
    height: 1200px;
    overflow: hidden;
    background: var(--canvas);
  }
  .sheet {
    position: relative;
    width: 1200px;
    height: 1200px;
  }
  .card {
    position: absolute;
    background: var(--blush);
    overflow: hidden;
  }
  .card--front {
    left: 30px;
    top: 89px;
    width: 518px;
    height: 296px;
  }
  .card--back {
    left: 588px;
    top: 94px;
    width: 517px;
    height: 295px;
  }
  .brand-dot {
    position: absolute;
    border-radius: 50%;
    background: var(--mark);
  }
  .card--front .brand-dot {
    left: 185px;
    top: 40px;
    width: 140px;
    height: 140px;
  }
  .card--back .brand-dot {
    left: 52px;
    top: 82px;
    width: 100px;
    height: 100px;
  }
  .brand-name {
    position: absolute;
    margin: 0;
    font-family: "Marcellus", serif;
    font-weight: 400;
    letter-spacing: 0.5px;
    white-space: nowrap;
    text-align: center;
  }
  .card--front .brand-name {
    left: 0;
    right: 0;
    top: 240px;
    font-size: 27px;
    color: var(--white);
  }
  .card--back .brand-name {
    left: 30px;
    width: 160px;
    top: 202px;
    font-size: 19px;
    color: var(--leaf);
  }
  .contact {
    position: absolute;
    right: 48px;
    top: 98px;
    text-align: right;
    color: var(--leaf);
  }
  .contact__name,
  .contact__role {
    margin: 0;
    font-family: "Marcellus", serif;
    font-weight: 400;
    font-size: 19px;
    line-height: 26px;
    letter-spacing: 0.3px;
    white-space: nowrap;
  }
  .contact__details {
    margin: 26px 0 0;
    font-family: "Didact Gothic", sans-serif;
    font-size: 14px;
    line-height: 18.5px;
    font-style: normal;
    white-space: nowrap;
  }
  .band {
    position: absolute;
    left: 0;
    right: 0;
    bottom: 0;
    height: 27px;
    background: var(--band);
  }
</style>
</head>
<body>
<main class="sheet">
  <section class="card card--front" aria-label="Card front">
    <span class="brand-dot" aria-hidden="true"></span>
    <h1 class="brand-name">PLUM TWIST</h1>
  </section>

  <section class="card card--back" aria-label="Card back">
    <span class="brand-dot" aria-hidden="true"></span>
    <p class="brand-name">PLUM TWIST</p>
    <div class="contact">
      <p class="contact__name">DERYA KAPLAN</p>
      <p class="contact__role">Store Manager</p>
      <address class="contact__details">
        ABN 41027395816<br>
        Lindencourt St. No:4 Sydney<br>
        +61 2 5550 4873<br>
        derya@mailbox.com
      </address>
    </div>
    <div class="band" aria-hidden="true"></div>
  </section>
</main>
</body>
</html>
```